Larkspur Stillness

Logo picture and I want it to say

yoga. meditation. sound healing

small sweet classes

Larkspur-stillness.com

2740 West Hollander Ave Suite K
Alder Cove ca 94021

```html
<!DOCTYPE html>
<html lang="en">
<head>
<meta charset="utf-8">
<title>Larkspur Stillness – Small Sweet Classes</title>
<link href="https://fonts.googleapis.com/css2?family=Cinzel:wght@500&family=Montserrat:wght@400&family=Oswald:wght@600&display=swap" rel="stylesheet">
<style>
  :root {
    --page-bg: #e9e6ec;
    --rose: #d56fa6;
    --orchid: #a45fb6;
    --violet: #7b4fae;
    --ink-light: #fbf4fb;
    --line-soft: rgba(255, 235, 250, 0.55);
    --ornament-tint: rgba(255, 225, 245, 0.16);
    --photo-light: #dcd8de;
    --photo-mid: #9a9aa3;
    --photo-dark: #3b3a40;
  }
  * { box-sizing: border-box; margin: 0; padding: 0; }
  html, body { width: 1200px; height: 800px; overflow: hidden; }
  body {
    background: var(--page-bg);
    display: flex;
    align-items: center;
    justify-content: center;
  }
  .flyer {
    position: relative;
    width: 540px;
    height: 764px;
    overflow: hidden;
    background: linear-gradient(150deg, var(--rose) 0%, var(--orchid) 45%, var(--violet) 100%);
    box-shadow: 0 6px 24px rgba(60, 30, 80, 0.18);
    color: var(--ink-light);
  }
  .flyer__art {
    position: absolute;
    inset: 0;
  }
  .brand {
    position: absolute;
    top: 128px;
    left: 50%;
    transform: translateX(-50%);
    width: 136px;
    height: 136px;
    border: 2px solid var(--line-soft);
    border-radius: 50%;
    display: flex;
    align-items: center;
    justify-content: center;
    text-align: center;
  }
  .brand__name {
    font-family: 'Montserrat', sans-serif;
    font-weight: 400;
    font-size: 15px;
    line-height: 1.25;
    letter-spacing: 0.04em;
    color: var(--ink-light);
  }
  .copy {
    position: absolute;
    top: 290px;
    left: 0;
    width: 100%;
    text-align: center;
  }
  .copy__tagline {
    font-family: 'Oswald', sans-serif;
    font-weight: 600;
    font-size: 17px;
    letter-spacing: 0.05em;
    text-transform: uppercase;
  }
  .copy__headline {
    margin-top: 8px;
    font-family: 'Cinzel', serif;
    font-weight: 500;
    font-size: 38px;
    letter-spacing: 0.03em;
    text-transform: uppercase;
  }
  .copy__address {
    margin-top: 12px;
    font-family: 'Montserrat', sans-serif;
    font-weight: 400;
    font-size: 19px;
    line-height: 1.3;
  }
  .copy__web {
    margin-top: 14px;
    font-family: 'Montserrat', sans-serif;
    font-weight: 400;
    font-size: 13px;
    letter-spacing: 0.02em;
  }
</style>
</head>
<body>
  <main class="flyer">
    <svg class="flyer__art" width="540" height="764" viewBox="0 0 540 764">
      <defs>
        <linearGradient id="photoTone" x1="0" y1="0" x2="1" y2="1">
          <stop offset="0" stop-color="var(--photo-light)"/>
          <stop offset="0.55" stop-color="var(--photo-mid)"/>
          <stop offset="1" stop-color="var(--photo-dark)"/>
        </linearGradient>
      </defs>
      <path class="ornament ornament--corner" role="img" aria-label="Decorative paisley ornament, top right corner"
            d="M300 0 H540 V230 Q430 210 380 140 Q320 80 300 0 Z" fill="var(--ornament-tint)"/>
      <path class="ornament ornament--edge" role="img" aria-label="Decorative paisley ornament along the left edge"
            d="M0 210 Q110 250 130 340 Q120 430 0 500 Z" fill="var(--ornament-tint)"/>
      <circle class="ornament ornament--halo" role="img" aria-label="Decorative petal ornament framing the class photo"
              cx="380" cy="860" r="380" fill="var(--ornament-tint)"/>
      <circle class="photo-frame" cx="380" cy="860" r="318" fill="none" stroke="var(--line-soft)" stroke-width="3"/>
      <circle class="photo" role="img" aria-label="Photo of a small group class meditating cross-legged on mats with hands at heart centre"
              cx="380" cy="860" r="312" fill="url(#photoTone)"/>
    </svg>

    <div class="brand">
      <span class="brand__name">Larkspur<br>Stillness</span>
    </div>

    <section class="copy">
      <p class="copy__tagline">Yoga . Meditation . Sound Healing</p>
      <h1 class="copy__headline">Small Sweet Classes</h1>
      <p class="copy__address">2740 West Hollander Ave Suite K<br>Alder Cove ca 94021</p>
      <p class="copy__web">www.larkspur-stillness.com</p>
    </section>
  </main>
</body>
</html>
```